Certificate Design for Employee Loyalty

We're a digital marketing agency in Australia (www.brightkitestudio.com.au) and we're looking to create a design for a certificate to celebrate employees who reach 5 years with us (we have a few coming up soon).
Ideally we'd want something that captures our funky, digital agency culture (see our Facebook page www.facebook.com/brightkitestudio for what we mean) and not be too "corporatey"
A4 portrait or landscape designs would be awesome, with spots for employee's name, a brief 2-3 line message and a design that reflects our culture and the 5 year milestone for the employee.
Any questions, please post!
Target Market(s)
Digital marketing employees.

```html
<!DOCTYPE html>
<html lang="en">
<head>
<meta charset="utf-8">
<title>5 Years of Service Award – Lumenfold</title>
<link rel="stylesheet" href="https://fonts.googleapis.com/css2?family=Bebas+Neue&display=swap">
<style>
  :root {
    --ink: #000000;
    --paper: #fbfbe9;
    --accent: #cc1408;
    --logo-text: #ffffff;
    --logo-bg-inner: #3a3a3a;
    --logo-bg-outer: #050505;
  }
  * { margin: 0; padding: 0; box-sizing: border-box; }
  html, body {
    width: 849px;
    height: 1200px;
    overflow: hidden;
    background: var(--ink);
  }
  .certificate {
    position: relative;
    width: 849px;
    height: 1200px;
    background: var(--ink);
    font-family: "Bebas Neue", "Oswald", sans-serif;
    color: var(--ink);
  }
  .certificate__panel {
    position: absolute;
    left: 120px;
    top: 113px;
    width: 612px;
    height: 942px;
    background: var(--paper);
  }
  .line {
    position: absolute;
    left: 0;
    width: 849px;
    text-align: center;
    line-height: 1;
    white-space: nowrap;
    transform-origin: center top;
  }
  .line--year {
    top: 88px;
    left: 9px;
    font-size: 225px;
    color: var(--accent);
    letter-spacing: 2px;
    transform: scaleX(1.11);
  }
  .line--years { top: 301px; left: 1px; font-size: 142px; }
  .line--service { top: 411px; font-size: 107px; }
  .line--award { top: 495px; left: 20px; font-size: 103px; }
  .line--presented { top: 588px; left: 13px; font-size: 80px; transform: scaleX(0.89); }
  .line--name { top: 657px; font-size: 141px; letter-spacing: 1px; }
  .message {
    position: absolute;
    top: 800px;
    left: 10px;
    width: 849px;
    text-align: center;
    font-size: 64px;
    line-height: 50px;
    transform: scaleX(1.11);
    transform-origin: center top;
  }
  .logo-tab {
    position: absolute;
    left: 350px;
    top: 960px;
    width: 193px;
    height: 240px;
    background: var(--accent);
  }
  .logo-tile {
    position: absolute;
    left: 12px;
    top: 8px;
    width: 170px;
    height: 170px;
    background: radial-gradient(circle at 50% 50%, var(--logo-bg-inner) 0%, var(--logo-bg-outer) 75%);
    display: flex;
    align-items: center;
    justify-content: center;
  }
  .logo-name {
    font-family: "Bebas Neue", "Oswald", sans-serif;
    font-size: 40px;
    line-height: 1;
    color: var(--logo-text);
    letter-spacing: 1px;
  }
</style>
</head>
<body>
  <main class="certificate">
    <div class="certificate__panel"></div>

    <div class="line line--year">2014</div>
    <h1 class="line line--years">5 Years</h1>
    <div class="line line--service">Of Service</div>
    <div class="line line--award">Award</div>
    <div class="line line--presented">Presented To</div>
    <div class="line line--name">Lorem Ipsum</div>
    <p class="message">For your outstanding<br>contribution to our<br>company</p>

    <div class="logo-tab">
      <div class="logo-tile">
        <span class="logo-name">Lumenfold</span>
      </div>
    </div>
  </main>
</body>
</html>
```